Home inspection business! professional look attracting customers just by looks. Read must haves

its a new business I started on my own for home inspections I would like something very professional to give to real estate agents and clients, its going to have my license number on it my business phone number my name my website as well etc on the back side it will be servicing areas and also what kind of services I offer I also have a business card from someone else the way I would like mine to be. I will attach my logo

Industry/Entity Type

Home Inspection

Contact Information for Business Card

listed in nice to haves

Requirements
Must have
• phone number - 718 352 9047
• website- crestwoodlatch.example
• license number #2749035186
• my name Gavin teraskovic
• picture of my logo and me on the front
• on the back of the card. stating I am servicing All of New York and Long Island
• also services I will offer will be home inspection -mold inspection -lead inspection -radon inspection -Termite Inspection -Infared Scan.
• and also we provide inspections for single family homes condos co-ops town-homes
• and commercial property
Nice to have
• same colors as the logos and also if you recommend fonts to look like the logo not sure up to you

```html
<!DOCTYPE html>
<html lang="en">
<head>
<meta charset="utf-8">
<title>Crestwood Latch – Business Cards</title>
<link rel="stylesheet" href="https://fonts.googleapis.com/css2?family=Montserrat:wght@600;700&family=Open+Sans:wght@400;600&display=swap">
<style>
  :root {
    --bg: #3b3b3d;
    --card: #29292b;
    --blue: #4aa0e2;
    --white: #f2f2f2;
    --grey: #9a9a9c;
    --photo-top: #5a5d63;
    --photo-bottom: #3a3c40;
  }
  * { box-sizing: border-box; margin: 0; padding: 0; }
  html, body { width: 1200px; height: 960px; overflow: hidden; }
  body {
    background: var(--bg);
    font-family: "Open Sans", sans-serif;
    color: var(--white);
    position: relative;
  }
  .card {
    position: absolute;
    left: 220px;
    width: 760px;
    height: 420px;
    background: var(--card);
    overflow: hidden;
  }
  .card--services { top: 45px; }
  .card--contact { top: 495px; }
  .card__band {
    position: absolute;
    left: 0; right: 0; bottom: 0;
    height: 14px;
    background: var(--blue);
  }
  .brand {
    display: flex;
    align-items: center;
    gap: 14px;
    font-family: "Montserrat", sans-serif;
    font-weight: 700;
    font-size: 34px;
    letter-spacing: 1px;
    color: var(--white);
    text-transform: uppercase;
    white-space: nowrap;
  }
  .brand__dot {
    width: 26px; height: 26px;
    border-radius: 50%;
    background: var(--blue);
    flex: none;
  }
  /* services side */
  .card--services .brand {
    position: absolute;
    top: 56px; left: 0; right: 0;
    justify-content: center;
  }
  .services {
    position: absolute;
    top: 138px; left: 0; right: 0;
    text-align: center;
  }
  .services__title {
    font-family: "Montserrat", sans-serif;
    font-weight: 700;
    font-size: 24px;
    color: var(--blue);
    margin-bottom: 12px;
  }
  .services__row {
    font-size: 20px;
    line-height: 36px;
  }
  .services__row span + span::before {
    content: "•";
    color: var(--blue);
    margin: 0 12px;
  }
  .coverage {
    position: absolute;
    top: 298px; left: 0; right: 0;
    text-align: center;
  }
  .coverage__area {
    font-family: "Montserrat", sans-serif;
    font-weight: 600;
    font-size: 18px;
    color: var(--blue);
    line-height: 28px;
  }
  .coverage__types {
    font-size: 16px;
    line-height: 28px;
    color: var(--white);
  }
  /* contact side */
  .owner-photo {
    position: absolute;
    top: 60px; left: 150px;
    width: 110px; height: 110px;
    border-radius: 50%;
    background: linear-gradient(180deg, var(--photo-top), var(--photo-bottom));
    border: 3px solid var(--blue);
  }
  .card--contact .brand {
    position: absolute;
    top: 205px; left: 48px;
    font-size: 26px;
  }
  .card--contact .brand__dot { width: 20px; height: 20px; }
  .divider {
    position: absolute;
    left: 400px; top: 80px;
    width: 1px; height: 230px;
    background: var(--grey);
  }
  .contact {
    position: absolute;
    left: 432px; top: 92px;
  }
  .contact__name {
    font-family: "Montserrat", sans-serif;
    font-weight: 600;
    font-size: 26px;
    color: var(--blue);
    text-transform: uppercase;
    margin-bottom: 20px;
  }
  .contact__line {
    display: flex;
    align-items: center;
    gap: 12px;
    font-size: 19px;
    line-height: 36px;
  }
  .contact__line svg { width: 18px; height: 18px; flex: none; }
  .contact__line .accent { color: var(--blue); }
  .contact__license {
    font-size: 19px;
    margin-top: 10px;
  }
</style>
</head>
<body>
  <section class="card card--services">
    <div class="brand"><span class="brand__dot"></span>Crestwood Latch</div>
    <div class="services">
      <h2 class="services__title">SERVICES</h2>
      <p class="services__row"><span>Home Inspection</span><span>Mold Inspection</span><span>Lead Inspection</span></p>
      <p class="services__row"><span>Radon Inspection</span><span>Termite Inspection</span><span>Infared Scan</span></p>
    </div>
    <div class="coverage">
      <p class="coverage__area">Servicing All of New York &amp; Long Island</p>
      <p class="coverage__types">Single Family Homes · Condos · Co-ops · Town-homes · Commercial Property</p>
    </div>
    <div class="card__band"></div>
  </section>

  <section class="card card--contact">
    <div class="owner-photo" role="img" aria-label="Portrait photo of the inspector"></div>
    <div class="brand"><span class="brand__dot"></span>Crestwood Latch</div>
    <div class="divider"></div>
    <div class="contact">
      <h1 class="contact__name">Gavin Teraskovic</h1>
      <p class="contact__line">
        <svg viewBox="0 0 24 24" aria-hidden="true"><path fill="#4aa0e2" d="M6.6 10.8a15 15 0 0 0 6.6 6.6l2.2-2.2a1 1 0 0 1 1-.25 11.4 11.4 0 0 0 3.6.57 1 1 0 0 1 1 1V20a1 1 0 0 1-1 1A17 17 0 0 1 3 4a1 1 0 0 1 1-1h3.5a1 1 0 0 1 1 1c0 1.25.2 2.45.57 3.57a1 1 0 0 1-.25 1z"/></svg>
        718 352 9047
      </p>
      <p class="contact__line">
        <svg viewBox="0 0 24 24" aria-hidden="true"><rect x="3" y="5" width="18" height="14" rx="1.5" fill="none" stroke="#4aa0e2" stroke-width="2"/><path d="M3 6l9 7 9-7" fill="none" stroke="#4aa0e2" stroke-width="2"/></svg>
        info@crestwoodlatch.example
      </p>
      <p class="contact__line">
        <svg viewBox="0 0 24 24" aria-hidden="true"><circle cx="12" cy="12" r="9" fill="none" stroke="#4aa0e2" stroke-width="2"/><path d="M3 12h18M12 3c3 3 3 15 0 18M12 3c-3 3-3 15 0 18" fill="none" stroke="#4aa0e2" stroke-width="1.6"/></svg>
        <span>www.<span class="accent">crestwoodlatch</span>.example</span>
      </p>
      <p class="contact__license">license number #2749035186</p>
    </div>
    <div class="card__band"></div>
  </section>
</body>
</html>
```